Design for "Vellow" protein health bars wrappers

I need a new design for a protein bar that my partners and I are launching for the North American and European markets.
The bar's name is "Vellow."
Given the masculine/aggressive nature of that name, we are thinking of neutralizing it with a more feminine/soft font and design. But hey - the sky is the limit. We obviously want this 20-gram protein bar to sell to a wide net (not just men but women also). So if it means having a Pellam Comic font/design (or whatever) in order to do this, so be it. I leave it up to your intelligence and experience.

ADDED ON FEBRUARY 24:

The official name of the bar is just "VELLOW" (not "Vellow Protein").

We have six flavors divided into two categories, which are 1) SOFT and 2) CRUNCHY.
So, the idea is to make two similar designs for the wrapper that still distinguish themselves from each other because one is 'soft' and the other is 'crunchy.'
Then, within each category, the idea is to have three color variations, designating the three flavors in each category.

Please look at the dimensions and examples of the generic wrapper designs that we already have (and which we find too generic), which I have uploaded.

Target Market(s)

North America - Brindle, Fair Harvest
Europe - Norway, Sweden, Denmark, Germany, France, Switzerland, Italy.

Industry/Entity Type

Nutrition

Logo Text

Vellow

Font styles to use
Serif
Decorative

Colors
fff6dc
f04a50

Requirements
Must have
• The title is "Vellow".
• We have six flavors divided into two categories, which are 1) SOFT and 2) CRUNCHY.
• You can work on the two different types of similar-but-different designs for the "soft" and for the "cruncy." Then it's just a question of color variations for each flavor.
• The flavors are:
• SOFT: 1) strawberry, 2) Chocolate brownie, 3) Cinnamon Crunch
• CRUNCY: 1) Peanut, 2) Lemon, 3) Coconut.
• On the side or at the bottom, there should be stated:
• "20 gm protein"
• "children friendly"
Nice to have
• Obvious: a design that catches the eye and inspires someone to buy the bar to eat it.
• Part of the design could include a photograph of the actual bar (you can use generic photos for that until we place a pic of the actual bar). Like 1/4th of the total surface (or even a little smaller).

```html
<!DOCTYPE html>
<html lang="en">
<head>
<meta charset="utf-8">
<title>Vellow Crunchy Protein Bar Wrappers</title>
<link rel="stylesheet" href="https://fonts.googleapis.com/css2?family=Archivo+Black&family=Fira+Sans+Extra+Condensed:wght@400;500&family=Fira+Sans+Condensed:wght@400&display=swap">
<style>
  :root {
    --canvas: #f1f1f1;
    --wrapper: #ffffff;
    --crimp-line: #e2e2e2;
    --ink: #161616;
    --muted: #2b2b2b;
    --peanut: #bb7a2c;
    --peanut-tint: #fbf3e8;
    --lemon: #8dc63f;
    --lemon-text: #6e9a36;
    --lemon-tint: #f5faec;
    --coconut: #72cfbe;
    --coconut-text: #4f9a8c;
    --coconut-tint: #eef9f6;
    --bar-light: #c79a72;
    --bar-dark: #8a5a3a;
  }
  * { box-sizing: border-box; margin: 0; padding: 0; }
  html, body {
    width: 920px; height: 1200px; overflow: hidden;
    background: var(--canvas);
  }
  .canvas { position: relative; width: 920px; height: 1200px; }

  .wrapper {
    position: absolute; left: 30px; width: 860px; height: 300px;
    background: var(--wrapper);
  }
  .wrapper--peanut  { top: 50px;  --accent: var(--peanut);  --accent-text: var(--peanut);       --tint: var(--peanut-tint); }
  .wrapper--lemon   { top: 440px; --accent: var(--lemon);   --accent-text: var(--lemon-text);   --tint: var(--lemon-tint); }
  .wrapper--coconut { top: 830px; --accent: var(--coconut); --accent-text: var(--coconut-text); --tint: var(--coconut-tint); }

  .crimp {
    position: absolute; top: 0; bottom: 0; width: 44px;
    background: repeating-linear-gradient(90deg, var(--wrapper) 0 4px, var(--crimp-line) 4px 6px);
  }
  .crimp--left { left: 0; }
  .crimp--right { right: 0; }

  .pattern-field {
    position: absolute; left: 20px; top: 12px; width: 480px; height: 205px;
    background: var(--tint);
  }

  .brand-name {
    position: absolute; left: 133px; top: 70px;
    font-family: "Archivo Black", sans-serif;
    font-size: 76px; line-height: 1; letter-spacing: -1px;
    color: var(--ink);
  }

  .category-band {
    position: absolute; left: 133px; top: 163px; width: 292px; height: 34px;
    background: var(--accent);
    color: #fff;
    font-family: "Fira Sans Extra Condensed", sans-serif;
    font-weight: 500; font-size: 29px; line-height: 34px;
    padding-left: 6px; white-space: nowrap;
  }

  .flavor {
    position: absolute; left: 236px; top: 228px;
    font-family: "Fira Sans Extra Condensed", sans-serif;
    font-weight: 500; font-size: 29px; line-height: 1;
    color: var(--accent-text);
  }

  .bar-photo {
    position: absolute; left: 518px; top: 66px; width: 292px; height: 136px;
    background: linear-gradient(160deg, var(--bar-light) 0%, #e0b36a 45%, #efe6d6 70%, var(--bar-dark) 100%);
    border-radius: 6px;
  }

  .protein-badge {
    position: absolute; left: 530px; top: 206px; width: 72px; height: 72px;
  }
  .protein-badge__text {
    position: absolute; inset: 0;
    display: flex; flex-direction: column; align-items: center; justify-content: center;
    font-family: "Fira Sans Condensed", sans-serif;
    font-size: 16px; line-height: 1.35; color: var(--muted);
  }

  .children-note {
    position: absolute; left: 624px; top: 228px;
    font-family: "Fira Sans Condensed", sans-serif;
    font-size: 23px; line-height: 1; color: var(--muted);
  }
</style>
</head>
<body>
<main class="canvas">

  <section class="wrapper wrapper--peanut">
    <div class="crimp crimp--left"></div>
    <div class="crimp crimp--right"></div>
    <div class="pattern-field" role="img" aria-label="Fine peanut-coloured zigzag line pattern"></div>
    <h1 class="brand-name">VELLOW</h1>
    <div class="category-band">CRUNCHY PROTEIN BAR</div>
    <p class="flavor">PEANUT</p>
    <div class="bar-photo" role="img" aria-label="Photo of a chocolate-coated protein bar cut open to show caramel and crunchy filling"></div>
    <div class="protein-badge">
      <svg width="72" height="72" viewBox="0 0 72 72">
        <path d="M58 22 A30 30 0 1 0 62 44" fill="none" stroke="#2b2b2b" stroke-width="1.6"/>
        <path d="M62 44 L66 30 M62 44 L56 34" fill="none" stroke="#2b2b2b" stroke-width="1.6"/>
      </svg>
      <div class="protein-badge__text"><span>20 gm</span><span>protein</span></div>
    </div>
    <p class="children-note">Children friendly</p>
  </section>

  <section class="wrapper wrapper--lemon">
    <div class="crimp crimp--left"></div>
    <div class="crimp crimp--right"></div>
    <div class="pattern-field" role="img" aria-label="Fine lime-green zigzag line pattern"></div>
    <h1 class="brand-name">VELLOW</h1>
    <div class="category-band">CRUNCHY PROTEIN BAR</div>
    <p class="flavor">LEMON</p>
    <div class="bar-photo" role="img" aria-label="Photo of a chocolate-coated protein bar cut open to show caramel and crunchy filling"></div>
    <div class="protein-badge">
      <svg width="72" height="72" viewBox="0 0 72 72">
        <path d="M58 22 A30 30 0 1 0 62 44" fill="none" stroke="#2b2b2b" stroke-width="1.6"/>
        <path d="M62 44 L66 30 M62 44 L56 34" fill="none" stroke="#2b2b2b" stroke-width="1.6"/>
      </svg>
      <div class="protein-badge__text"><span>20 gm</span><span>protein</span></div>
    </div>
    <p class="children-note">Children friendly</p>
  </section>

  <section class="wrapper wrapper--coconut">
    <div class="crimp crimp--left"></div>
    <div class="crimp crimp--right"></div>
    <div class="pattern-field" role="img" aria-label="Fine aqua zigzag line pattern"></div>
    <h1 class="brand-name">VELLOW</h1>
    <div class="category-band">CRUNCHY PROTEIN BAR</div>
    <p class="flavor">COCONUT</p>
    <div class="bar-photo" role="img" aria-label="Photo of a chocolate-coated protein bar cut open to show caramel and crunchy filling"></div>
    <div class="protein-badge">
      <svg width="72" height="72" viewBox="0 0 72 72">
        <path d="M58 22 A30 30 0 1 0 62 44" fill="none" stroke="#2b2b2b" stroke-width="1.6"/>
        <path d="M62 44 L66 30 M62 44 L56 34" fill="none" stroke="#2b2b2b" stroke-width="1.6"/>
      </svg>
      <div class="protein-badge__text"><span>20 gm</span><span>protein</span></div>
    </div>
    <p class="children-note">Children friendly</p>
  </section>

</main>
</body>
</html>
```